Business Cards Needed for Innovative Healthcare Marketing Company

We are a marketing company focused on healthcare. Our company is all about rebranding yourself renewing your image and generating results. The phoenix stands for "reborn" or "rising" which we provide new brands for our clients we take their old brands and renew it with creativity and innovation. I am looking for a business card with color dimension. I have attached an example of a card I think has the look and feel of what I am trying to accomplish. I like that the card example has black and grey font colors, I like the font placement and the small logo, I really like the use of the colors on the right those are the colors of my logo. My logo is phoenix so maybe incorporating flames similar to that design. I would like the back a solid color maybe red with an opaque version of the logo and website. As a marketing company I am always open to creative liberty!

Target Market(s)

Doctors and business professionals.

Industry/Entity Type

Marketing

Contact Information for Business Card

Velmora Health Care Marketing
Dana Prewitt- CEO
#(407)555-0172
email-dana@velmora.com
website- velmora.com

Font styles to use
Sans Serif

Colors
ec1f27
f37122
ffc214
fbed22
fbf289
f04a50

Requirements
Must have
• The logo and required information
Nice to have
• icons by the information
Should not have
• child like font

```html
<!DOCTYPE html>
<html lang="en">
<head>
<meta charset="utf-8">
<title>Velmora Health Care Marketing — Business Card</title>
<link rel="stylesheet" href="https://fonts.googleapis.com/css2?family=Open+Sans:wght@300;400;600;700&display=swap">
<style>
  :root {
    --page-bg: #2b2d31;
    --card-white: #ffffff;
    --red-deep: #9e1b20;
    --red: #c8262b;
    --orange: #f37122;
    --amber: #f7941d;
    --brand-red: #a3232a;
    --name-orange: #c8501c;
    --ink: #2a2a2a;
    --ghost: #e6e6e6;
    --ghost-soft: #f4f4f4;
  }
  * { box-sizing: border-box; margin: 0; padding: 0; }
  html, body { width: 1200px; height: 864px; overflow: hidden; }
  body {
    background: var(--page-bg);
    font-family: "Open Sans", Arial, sans-serif;
    display: flex;
    flex-direction: column;
    align-items: center;
    justify-content: center;
    gap: 40px;
  }
  .card {
    position: relative;
    width: 600px;
    height: 343px;
    overflow: hidden;
  }

  /* Back of card */
  .card--back {
    background: radial-gradient(ellipse 55% 75% at 50% 42%, var(--amber) 0%, var(--orange) 30%, var(--red) 70%, var(--red-deep) 100%);
    color: #fff;
  }
  .card--back .emblem-area {
    position: absolute;
    left: 190px; top: 20px;
    width: 220px; height: 290px;
    border-radius: 50%;
    background: radial-gradient(ellipse at center, rgba(255,190,90,0.35), rgba(255,190,90,0) 70%);
  }
  .card--back .wordmark {
    position: absolute;
    left: 0; right: 0; top: 112px;
    text-align: center;
  }
  .card--back .wordmark__name {
    font-weight: 300;
    font-size: 58px;
    letter-spacing: 3px;
    line-height: 1;
  }
  .card--back .wordmark__rule {
    width: 300px; height: 1px;
    margin: 8px auto 6px;
    background: rgba(255,255,255,0.8);
  }
  .card--back .wordmark__tagline {
    font-weight: 300;
    font-size: 18px;
    letter-spacing: 1.5px;
  }

  /* Front of card */
  .card--front { background: var(--card-white); color: var(--ink); }
  .card--front .emblem-area {
    position: absolute;
    left: 0; top: 0;
    width: 250px; height: 343px;
    background: radial-gradient(ellipse 70% 60% at 40% 45%, var(--ghost) 0%, var(--ghost-soft) 55%, rgba(255,255,255,0) 100%);
  }
  .brand {
    position: absolute;
    left: 300px; top: 50px;
    display: flex;
    align-items: center;
    gap: 12px;
    color: var(--brand-red);
  }
  .brand__dot {
    width: 58px; height: 58px;
    border-radius: 50%;
    background: var(--orange);
    flex: none;
  }
  .brand__text { width: 230px; }
  .brand__name {
    font-weight: 300;
    font-size: 44px;
    letter-spacing: 2px;
    line-height: 1;
  }
  .brand__rule { height: 1px; background: var(--brand-red); margin: 5px 0 3px; }
  .brand__tagline { font-weight: 300; font-size: 14px; letter-spacing: 1px; }

  .person { position: absolute; left: 270px; top: 158px; }
  .person__name { font-weight: 700; font-size: 19px; color: var(--name-orange); }
  .person__role { font-size: 13px; margin-top: 2px; }

  .contact {
    position: absolute;
    left: 262px; top: 240px;
    list-style: none;
    font-size: 15px;
    line-height: 24px;
  }
  .contact li { display: flex; align-items: center; gap: 10px; }
  .contact svg { width: 13px; height: 13px; flex: none; }
</style>
</head>
<body>

  <section class="card card--back" aria-label="Business card back">
    <div class="emblem-area" role="img" aria-label="Faint rising phoenix emblem behind the company name"></div>
    <div class="wordmark">
      <div class="wordmark__name">VELMORA</div>
      <div class="wordmark__rule"></div>
      <div class="wordmark__tagline">HEALTH CARE MARKETING</div>
    </div>
  </section>

  <section class="card card--front" aria-label="Business card front">
    <div class="emblem-area" role="img" aria-label="Faint grey phoenix wing decoration"></div>

    <div class="brand">
      <span class="brand__dot"></span>
      <div class="brand__text">
        <div class="brand__name">VELMORA</div>
        <div class="brand__rule"></div>
        <div class="brand__tagline">HEALTH CARE MARKETING</div>
      </div>
    </div>

    <div class="person">
      <div class="person__name">Dana Prewitt</div>
      <div class="person__role">CEO</div>
    </div>

    <ul class="contact">
      <li>
        <svg viewBox="0 0 16 16" aria-hidden="true"><path fill="#f37122" d="M3.6 1.2l2.3 2.6-1.3 1.9c.9 2 2.6 3.7 4.6 4.6l1.9-1.3 2.6 2.3-1.2 2.4C7 13.5 2.5 9 1.2 2.4z"/></svg>
        <span>(407)555-0172</span>
      </li>
      <li>
        <svg viewBox="0 0 16 16" aria-hidden="true"><rect x="1" y="3" width="14" height="10" fill="#f37122"/><path d="M1 3l7 6 7-6" fill="none" stroke="#fff" stroke-width="1.3"/></svg>
        <span>dana@velmora.com</span>
      </li>
      <li>
        <svg viewBox="0 0 16 16" aria-hidden="true"><circle cx="8" cy="8" r="7" fill="#f37122"/><path d="M1 8h14M8 1c3 3 3 11 0 14M8 1c-3 3-3 11 0 14" fill="none" stroke="#fff" stroke-width="1"/></svg>
        <span>www.velmora.com</span>
      </li>
    </ul>
  </section>

</body>
</html>
```